Endocrinologist needs new stationery

I have a logo from MarkForge and now need stationery with the new logo.

Address: Suite 4, 282 Falcon Street, Kellmore, VIC 3188
Phone: 03 9417 2253
Fax: 03 9417 2255
Website: www.drmaylacorwen.com.au
Email: admin@drmaylacorwen.com.au

```html
<!DOCTYPE html>
<html lang="en">
<head>
<meta charset="utf-8">
<title>Dr Mayla Corwen Endocrinology – Business Card</title>
<link rel="stylesheet" href="https://fonts.googleapis.com/css2?family=Lato:wght@400;700&display=swap">
<style>
  :root {
    --page-bg: #2a2a2c;
    --card-white: #ffffff;
    --blue-light: #4a8bb8;
    --blue-dark: #2c6a9a;
    --plum: #7d5470;
    --plum-deep: #6a4460;
    --teal: #5aa5be;
    --text-plum: #7a4a6a;
    --text-white: #ffffff;
  }
  * { box-sizing: border-box; margin: 0; padding: 0; }
  html, body {
    width: 1200px; height: 915px; overflow: hidden;
    background: var(--page-bg);
    font-family: "Lato", sans-serif;
  }
  .canvas { position: relative; width: 1200px; height: 915px; }

  .card {
    position: absolute; left: 290px;
    width: 620px; height: 379px;
    overflow: hidden;
  }

  /* Shared logo lockup: name over spaced specialty line and rule */
  .logo-lockup { position: absolute; white-space: nowrap; }
  .logo-name { font-weight: 400; letter-spacing: 1px; }
  .logo-specialty {
    display: flex; align-items: center;
    text-transform: uppercase; font-weight: 400;
  }
  .logo-specialty::after {
    content: ""; display: block; height: 1px;
    background: currentColor; opacity: .7;
  }

  /* Front side */
  .card-front {
    top: 52px;
    background: linear-gradient(135deg, var(--blue-light) 0%, var(--blue-dark) 100%);
    color: var(--text-white);
  }
  .card-front .logo-lockup { left: 130px; top: 96px; }
  .card-front .logo-name { font-size: 44px; line-height: 52px; padding-left: 30px; }
  .card-front .logo-specialty { font-size: 15px; letter-spacing: 10px; margin-top: 4px; }
  .card-front .logo-specialty::after { width: 80px; margin-left: 4px; }
  .card-front .website {
    position: absolute; left: 0; right: 0; top: 250px;
    text-align: center;
    font-size: 17px; font-weight: 700; letter-spacing: 4px;
  }

  /* Back side */
  .card-back {
    top: 484px;
    background: var(--card-white);
    color: var(--text-plum);
  }
  .side-band {
    position: absolute; left: 0; top: 0;
    width: 62px; height: 250px;
    background: var(--plum);
  }
  .corner-block {
    position: absolute; left: 0; top: 288px;
    width: 82px; height: 91px;
    background: var(--plum-deep);
  }
  .accent-band {
    position: absolute; right: 0; top: 282px;
    width: 196px; height: 36px;
    background: var(--teal);
  }
  .contact-list {
    position: absolute; left: 50px; top: 34px;
    list-style: none;
  }
  .contact-item {
    display: flex; align-items: flex-start;
    font-size: 17px; line-height: 21px; letter-spacing: .6px;
    margin-bottom: 8px;
  }
  .contact-icon {
    flex: none; width: 22px; height: 22px; margin-right: 14px; margin-top: 0;
  }
  .card-back .logo-lockup { left: 96px; top: 252px; color: var(--blue-dark); }
  .card-back .logo-name { font-size: 26px; line-height: 30px; padding-left: 14px; }
  .card-back .logo-specialty { font-size: 10px; letter-spacing: 7px; margin-top: 3px; color: var(--text-plum); }
  .card-back .logo-specialty::after { width: 56px; margin-left: 2px; }
</style>
</head>
<body>
<main class="canvas">

  <section class="card card-front" aria-label="Card front">
    <div class="logo-lockup">
      <p class="logo-name">Dr Mayla Corwen</p>
      <p class="logo-specialty">Endocrinology</p>
    </div>
    <p class="website">www.drmaylacorwen.com.au</p>
  </section>

  <section class="card card-back" aria-label="Card back">
    <div class="side-band"></div>
    <div class="corner-block"></div>
    <div class="accent-band"></div>

    <ul class="contact-list">
      <li class="contact-item">
        <svg class="contact-icon" viewBox="0 0 22 22" aria-hidden="true">
          <circle cx="11" cy="11" r="10" fill="#fff" stroke="#7d5470" stroke-width="1.2"/>
          <path d="M11 5.5a3.5 3.5 0 0 0-3.5 3.5c0 2.6 3.5 6.5 3.5 6.5s3.5-3.9 3.5-6.5A3.5 3.5 0 0 0 11 5.5z" fill="#7d5470"/>
          <circle cx="11" cy="9" r="1.3" fill="#fff"/>
        </svg>
        <span>Suite 4, 282 Falcon Street,<br>Kellmore, VIC 3188</span>
      </li>
      <li class="contact-item">
        <svg class="contact-icon" viewBox="0 0 22 22" aria-hidden="true">
          <circle cx="11" cy="11" r="10" fill="#fff" stroke="#7d5470" stroke-width="1.2"/>
          <path d="M8 6l2 2.5-1.2 1.3c.7 1.4 1.7 2.4 3.1 3.1L13.2 11.7 15.7 13.7 14.6 15.6C10.5 15.4 6.6 11.5 6.4 7.4z" fill="#7d5470"/>
        </svg>
        <span>03 9417 2253</span>
      </li>
      <li class="contact-item">
        <svg class="contact-icon" viewBox="0 0 22 22" aria-hidden="true">
          <circle cx="11" cy="11" r="10" fill="#fff" stroke="#7d5470" stroke-width="1.2"/>
          <rect x="8" y="5.5" width="6" height="3.5" fill="none" stroke="#7d5470" stroke-width="1.1"/>
          <rect x="6" y="9" width="10" height="4.5" rx="1" fill="#7d5470"/>
          <rect x="8" y="12.5" width="6" height="4" fill="#fff" stroke="#7d5470" stroke-width="1.1"/>
        </svg>
        <span>03 9417 2255</span>
      </li>
      <li class="contact-item">
        <svg class="contact-icon" viewBox="0 0 22 22" aria-hidden="true">
          <circle cx="11" cy="11" r="10" fill="#fff" stroke="#7d5470" stroke-width="1.2"/>
          <rect x="6" y="7.5" width="10" height="7" fill="#7d5470"/>
          <path d="M6 7.5l5 4 5-4" fill="none" stroke="#fff" stroke-width="1"/>
        </svg>
        <span>admin@drmaylacorwen.com.au</span>
      </li>
    </ul>

    <div class="logo-lockup">
      <p class="logo-name">Dr Mayla Corwen</p>
      <p class="logo-specialty">Endocrinology</p>
    </div>
  </section>

</main>
</body>
</html>
```